Velquist Values Chart

I am the CEO of Velquist http://velquist-example.com

I want to create a Values Chart for our new company and I have attached a PDF of an example of such chart that I really like.

The objective of the values chart is to visually and creatively summarize how the company and its employees will build their unique company identity.

I have also attached a word document with the Velquist logo and a visual that summarizes our business technology process. This visual can but does not have to be incorporated into the Values Chart. Below this visual are the statements that I have chosen to represent our values on the values chart.

Industry/Entity Type

Graphic Design

Requirements
Must have
• I would like the feel of this document to go along with the feel of our company website which I would describe as clean and crisp.

```html
<!DOCTYPE html>
<html lang="en">
<head>
<meta charset="utf-8">
<title>Velquist Values Chart</title>
<link rel="stylesheet" href="https://fonts.googleapis.com/css2?family=Oswald:wght@500;600;700&display=swap">
<style>
  :root {
    --bg-deep: #141414;
    --bg-soft: #2a2a2a;
    --lime: #8dc63f;
    --leaf: #3cb44b;
    --green: #1f9f52;
    --forest: #14934a;
    --jade: #1aa072;
    --teal: #13a08e;
    --sea: #0f9a9a;
  }
  html, body {
    margin: 0;
    padding: 0;
    overflow: hidden;
    background: var(--bg-deep);
  }
  .values-chart {
    position: relative;
    width: 851px;
    height: 1200px;
    overflow: hidden;
    background: radial-gradient(ellipse at 45% 40%, var(--bg-soft) 0%, #1e1e1e 55%, var(--bg-deep) 100%);
  }
  .value-cloud {
    position: absolute;
    inset: 0;
    width: 851px;
    height: 1200px;
  }
  .value-cloud text {
    font-family: "Oswald", "Arial Narrow", sans-serif;
    font-weight: 600;
    text-transform: uppercase;
  }
  .lime   { fill: var(--lime); }
  .leaf   { fill: var(--leaf); }
  .green  { fill: var(--green); }
  .forest { fill: var(--forest); }
  .jade   { fill: var(--jade); }
  .teal   { fill: var(--teal); }
  .sea    { fill: var(--sea); }
</style>
</head>
<body>
<main class="values-chart">
  <svg class="value-cloud" viewBox="0 0 851 1200" role="img" aria-label="Velquist company values chart">
    <title>Velquist Values</title>
    <g class="values-vertical">
      <text class="teal" font-size="56" textLength="630" lengthAdjust="spacingAndGlyphs" transform="translate(194 655) rotate(-90)">Play to win vs. play to participate</text>
      <text class="lime" font-size="57" textLength="471" lengthAdjust="spacingAndGlyphs" transform="translate(255 557) rotate(-90)">Cleanest people in waste</text>
      <text class="leaf" font-size="38" textLength="158" lengthAdjust="spacingAndGlyphs" transform="translate(304 294) rotate(-90)">Serve others</text>
      <text class="leaf" font-size="52" textLength="247" lengthAdjust="spacingAndGlyphs" transform="translate(316 548) rotate(-90)">Communicate</text>
      <text class="green" font-size="57" textLength="152" lengthAdjust="spacingAndGlyphs" transform="translate(380 542) rotate(-90)">Caring</text>
      <text class="lime" font-size="65" textLength="158" lengthAdjust="spacingAndGlyphs" transform="translate(448 538) rotate(-90)">Courage</text>
      <text class="lime" font-size="40" textLength="98" lengthAdjust="spacingAndGlyphs" transform="translate(495 115) rotate(-90)">Crisp</text>
      <text class="lime" font-size="61" textLength="344" lengthAdjust="spacingAndGlyphs" transform="translate(663 376) rotate(-90)">Keep things simple</text>
      <text class="leaf" font-size="55" textLength="804" lengthAdjust="spacingAndGlyphs" transform="translate(722 832) rotate(-90)">Passion for cost and production efficiency</text>
      <text class="leaf" font-size="35" textLength="170" lengthAdjust="spacingAndGlyphs" transform="translate(179 832) rotate(-90)">Irresistible</text>
      <text class="lime" font-size="32" textLength="90" lengthAdjust="spacingAndGlyphs" transform="translate(215 753) rotate(-90)">Offers</text>
      <text class="lime" font-size="56" textLength="149" lengthAdjust="spacingAndGlyphs" transform="translate(390 821) rotate(-90)">Connect</text>
      <text class="leaf" font-size="35" textLength="190" lengthAdjust="spacingAndGlyphs" transform="translate(189 1155) rotate(-90)">Strength based</text>
      <text class="teal" font-size="32" textLength="108" lengthAdjust="spacingAndGlyphs" transform="translate(732 1155) rotate(-90)">In approach</text>
    </g>
    <g class="values-horizontal">
      <text class="lime" x="208" y="75" font-size="52" textLength="220" lengthAdjust="spacingAndGlyphs">Raving fans</text>
      <text class="leaf" x="505" y="115" font-size="105" textLength="83" lengthAdjust="spacingAndGlyphs">W3</text>
      <text class="lime" x="273" y="123" font-size="45" textLength="148" lengthAdjust="spacingAndGlyphs">Give back</text>
      <text class="lime" x="316" y="204" font-size="82" textLength="284" lengthAdjust="spacingAndGlyphs">Cash flow</text>
      <text class="leaf" x="313" y="263" font-size="46" textLength="290" lengthAdjust="spacingAndGlyphs">Outstanding people</text>
      <text class="forest" x="330" y="370" font-size="116" textLength="270" lengthAdjust="spacingAndGlyphs">Be real</text>
      <text class="lime" x="459" y="448" font-size="65" textLength="210" lengthAdjust="spacingAndGlyphs">Speak the</text>
      <text class="lime" x="462" y="542" font-size="105" textLength="210" lengthAdjust="spacingAndGlyphs">Truth</text>
      <text class="leaf" x="208" y="606" font-size="51" textLength="438" lengthAdjust="spacingAndGlyphs">Bulletproof reliability</text>
      <text class="lime" x="201" y="657" font-size="46" textLength="466" lengthAdjust="spacingAndGlyphs">Turning problems into profits</text>
      <text class="lime" x="263" y="707" font-size="44" textLength="75" lengthAdjust="spacingAndGlyphs">Value</text>
      <text class="lime" x="258" y="753" font-size="44" textLength="79" lengthAdjust="spacingAndGlyphs">Added</text>
      <text class="leaf" x="205" y="799" font-size="44" textLength="139" lengthAdjust="spacingAndGlyphs">Marketing</text>
      <text class="forest" x="399" y="775" font-size="131" textLength="268" lengthAdjust="spacingAndGlyphs">Direct</text>
      <text class="green" x="395" y="825" font-size="51" textLength="268" lengthAdjust="spacingAndGlyphs">Communication</text>
      <text class="leaf" x="227" y="832" font-size="26" textLength="100" lengthAdjust="spacingAndGlyphs">Relentless</text>
      <text class="jade" x="158" y="893" font-size="70" textLength="241" lengthAdjust="spacingAndGlyphs">Passion</text>
      <text class="leaf" x="438" y="878" font-size="42" textLength="280" lengthAdjust="spacingAndGlyphs">Resourcefulness</text>
      <text class="teal" x="406" y="914" font-size="30" textLength="314" lengthAdjust="spacingAndGlyphs">You get what you focus on</text>
      <text class="lime" x="162" y="954" font-size="39" textLength="208" lengthAdjust="spacingAndGlyphs">Protecting the</text>
      <text class="lime" x="380" y="987" font-size="75" textLength="345" lengthAdjust="spacingAndGlyphs">Environment</text>
      <text class="leaf" x="201" y="993" font-size="35" textLength="155" lengthAdjust="spacingAndGlyphs">Model after</text>
      <text class="leaf" x="215" y="1043" font-size="39" textLength="133" lengthAdjust="spacingAndGlyphs">People far</text>
      <text class="sea" x="366" y="1042" font-size="52" textLength="366" lengthAdjust="spacingAndGlyphs">Powerful alliances</text>
      <text class="green" x="201" y="1105" font-size="61" textLength="175" lengthAdjust="spacingAndGlyphs">Greater</text>
      <text class="lime" x="208" y="1151" font-size="42" textLength="159" lengthAdjust="spacingAndGlyphs">Persistent</text>
      <text class="green" x="387" y="1151" font-size="117" textLength="311" lengthAdjust="spacingAndGlyphs">Flexible</text>
    </g>
  </svg>
</main>
</body>
</html>
```